Velvet Crest Car Detailing Brochure

I would like a trifold brochure designed for my car detailing business. The background has to be full black or mostly black with some designing using only colors present in our logo.

Front page must have our logo and name, list of services, a photo and mybe our phone number but no long text.

Inside I want to present each service one by one with its description and a photo representing/showing each service. (I will provide the text below). For photos, use stock photos and I will add come of mines already too.

On the back of the brochure I want to have contact & info: phone number, opening hours, address, website, Instagram.

Outside left I want the text About us and photo/design.

I want the brochure to be neat, professional, easy to read, but at the same time not too boring.

Text:
1. About us
a. the ultimate destination for car care in Geneva. We provide personalized, detail-oriented services that bring out the best in your car. With our expert techniques and dedicated approach, we ensure that your car receives the utmost care and attention. Experience a place where passion meets precision and let us create an exceptional car care experience designed just for you.
2. Services:

DETAILING & HAND WASH

• Comprehensive exterior & interior care
• Personalisation and tailored cleaning packages
• Decontamination
• Premium products
• Attention to detail for a perfect finish

POLISHING

• Eliminates scratches, holograms
• Revives and protects paint
• Ensures lasting gloss
• Enhances paint life
• Preserves car’s value and beauty

CERAMIC TREATMENT

• Durable paint protection
• Water-repellent (hydrophobic) effect
• Easier cleaning, enhanced shine
• Long-term surface safeguarding
• Shields against environmental impacts

DRY ICE WASH

• Innovative, waterless method
• Safe for all car parts
• Deep cleans, removes odors
• Allergen-free, antibacterial
• Gentle, effective
• Advanced cleaning technology

COVERING

• Personalized vehicle styling
• More than 150 colours available
• Clean cut without using a cutter
• High-quality, durable materials
• Custom designs available

PROTECTION FILM

• Invisible, durable shield
• Self-healing technology
• 10-year warranty by QR VONT

DETAILING BOUTIQUE

• Premium brands available
• Buy on site during your visit
• Marble Harbour, Zeb Autos, DRUP Polaro
• Essential for at-home car care
• Perfect for quick touch-ups
(for these three brands you can put their logos

Target Market(s)

Our target market includes car owners of all price ranges, with a special focus on those who are passionate about their vehicles. We cater to clients who value excellent service and results, and seek to maintain their cars in pristine condition.

Industry/Entity Type

Automobile / Car detailing

Colors

Designer to choose colors to be used in the design.

Requirements
Must have
• Brand Consistency: The brochure must adhere to our brand colors and style, particularly utilizing the colors present in our logo. Trifold Layout: The design must be specifically tailored for a trifold brochure format. Legibility: Text must be easy to read against the mostly black background, with appropriate font size and style. Professional Look and Feel: The overall design must convey professionalism while being engaging and not overly complex. Photo representation: each service description should have a phot presenting it.
Should not have
• Overcrowded Design: Avoid cluttering with too much text or too many images. The layout should be clean and easy to navigate. Cartoonish Fonts or Graphics: Avoid using unprofessional or casual fonts and graphics that do not align with the upscale and professional image of our business. Distracting Backgrounds: The background should complement and not overpower the content. Stick to the theme of mostly black with design elements from our logo.

```html
<!DOCTYPE html>
<html lang="en">
<head>
<meta charset="utf-8">
<title>Velvet Crest Car Detailing – Trifold Brochure</title>
<link href="https://fonts.googleapis.com/css2?family=Montserrat:ital,wght@0,400;0,500;0,600;0,700;0,800;1,500&family=Josefin+Sans:wght@300;400&display=swap" rel="stylesheet">
<style>
  :root{
    --page:#efefef;
    --black:#0c0a10;
    --black-soft:#16121c;
    --blue:#4f7fd3;
    --violet:#8a55bf;
    --magenta:#d43fa6;
    --pink:#e873c2;
    --heading:#b98be6;
    --text:#ecebf2;
    --muted:#b9b4c6;
    --white:#ffffff;
    --photo-dark:#3a3a42;
    --photo-mid:#8c8c96;
    --photo-light:#c9ccd3;
  }
  *{box-sizing:border-box;margin:0;padding:0}
  html,body{width:1200px;height:800px;overflow:hidden}
  body{background:var(--page);font-family:"Montserrat",sans-serif;color:var(--text);position:relative}

  .spread{position:absolute;left:30px;width:1140px;height:370px;display:flex;box-shadow:0 6px 18px rgba(0,0,0,.2)}
  .spread--outside{top:16px}
  .spread--inside{top:410px}
  .panel{width:380px;height:370px;position:relative;overflow:hidden;background:var(--black)}
  .panel + .panel{border-left:1px solid rgba(138,85,191,.35)}

  .photo{display:block;border-radius:2px;border:1px solid rgba(255,255,255,.12)}
  .photo--dark{background:linear-gradient(135deg,var(--photo-dark),#202026)}
  .photo--grey{background:linear-gradient(135deg,var(--photo-light),var(--photo-mid))}
  .photo--blue{background:linear-gradient(135deg,#8fb6e6,#3e5f8f)}
  .photo--colour{background:linear-gradient(120deg,#e45aa5,#6c7fd8,#58c2c9)}

  /* ---------- outside ---------- */
  .about{background:radial-gradient(circle at 0% 0%,rgba(79,127,211,.35),rgba(12,10,16,0) 55%),radial-gradient(circle at 100% 100%,rgba(212,63,166,.3),rgba(12,10,16,0) 55%),var(--black);padding:34px 30px}
  .about__type{font-weight:700;font-size:13px;color:var(--white)}
  .about__sector{font-style:italic;font-weight:500;font-size:9.5px;margin-bottom:20px;color:var(--pink)}
  .about__label{font-size:10.5px;font-weight:600;margin-bottom:6px;color:var(--heading)}
  .about__text{font-size:9.6px;line-height:1.5;text-align:justify;margin-bottom:22px;color:var(--text)}

  .contact__grid{display:grid;grid-template-columns:1fr 1fr;grid-template-rows:76px 76px;gap:6px;padding:8px;height:170px;background:var(--black-soft)}
  .contact__body{padding:16px 26px}
  .brandmark{display:flex;align-items:center;gap:8px;margin-bottom:10px}
  .brandmark__dot{width:20px;height:20px;border-radius:50%;border:2px solid var(--magenta)}
  .brandmark__name{font-family:"Josefin Sans",sans-serif;font-size:13px;letter-spacing:1px;color:var(--white)}
  .contact__line{font-size:9.6px;line-height:1.6;color:var(--text)}
  .contact__key{color:var(--pink);font-weight:600}

  .cover{color:var(--white)}
  .cover__top{position:absolute;left:0;top:0;width:380px;height:70px}
  .cover__bottom{position:absolute;left:0;bottom:0;width:380px;height:40px}
  .cover__brand{position:absolute;top:22px;left:0;right:0;display:flex;flex-direction:column;align-items:center;gap:8px}
  .cover__ring{width:64px;height:64px;border-radius:50%;background:var(--white);border:4px solid var(--pink)}
  .cover__name{font-family:"Josefin Sans",sans-serif;font-weight:300;font-size:22px;letter-spacing:2px;text-align:center;line-height:1.1}
  .cover__photo{position:absolute;left:90px;top:150px;width:200px;height:100px;border-radius:50%;background:radial-gradient(ellipse,#c8334a 0%,#7a2c63 45%,rgba(12,10,16,0) 72%)}
  .cover__services{position:absolute;left:0;right:0;top:252px;text-align:center;list-style:none;font-weight:800;font-size:11px;line-height:1.35;letter-spacing:.4px}

  /* ---------- inside ---------- */
  .inside{background:radial-gradient(circle at 0% 0%,rgba(212,63,166,.22),rgba(12,10,16,0) 50%),var(--black);padding:12px 16px}
  .inside--mid{background:radial-gradient(circle at 100% 100%,rgba(138,85,191,.28),rgba(12,10,16,0) 55%),var(--black);padding:0 0 8px}
  .inside--right{background:radial-gradient(circle at 100% 0%,rgba(79,127,211,.25),rgba(12,10,16,0) 50%),var(--black);padding:10px 16px}

  .services__title{font-weight:800;font-size:21px;color:var(--pink);letter-spacing:1px;text-align:center}
  .service__title{font-weight:700;font-size:12.5px;color:var(--heading);letter-spacing:.6px;margin:4px 0 5px}
  .service__title--center{text-align:center}
  .bullets{list-style:none;font-size:9.2px;line-height:1.28;font-weight:500;color:var(--text)}
  .bullets li{padding-left:9px;position:relative}
  .bullets li::before{content:"";position:absolute;left:1px;top:5px;width:3px;height:3px;border-radius:50%;background:var(--pink)}

  .pair{display:flex;gap:8px;margin-bottom:8px}
  .pair .photo{flex:1;height:66px}
  .row{display:flex;gap:10px;align-items:flex-start}

  .ceramic__photo{width:100%;height:104px;border-radius:0;border:none}
  .mid__body{padding:6px 16px 0}
  .dryice{display:flex;gap:10px;align-items:center;margin:6px 0 5px}
  .dryice__photo{width:110px;height:72px}
  .dryice__title{font-weight:700;font-size:13px;color:var(--heading);line-height:1.15}

  .brands{display:flex;gap:6px;margin:4px 0 4px 9px}
  .brands__badge{width:44px;height:16px;border-radius:2px;background:var(--white);border:1px solid #d8cde6}
  .brands__badge--dark{background:#2b2b31;border-color:#6a6474}
</style>
</head>
<body>

<!-- OUTSIDE -->
<section class="spread spread--outside">
  <article class="panel about">
    <p class="about__type">Industry/Entity Type</p>
    <p class="about__sector">Automobile / Car detailing</p>
    <p class="about__label">About us</p>
    <p class="about__text">The ultimate destination for car care in Geneva. We provide personalized, detail-oriented services that bring out the best in your car. With our expert techniques and dedicated approach, we ensure that your car receives the utmost care and attention. Experience a place where passion meets precision and let us create an exceptional car care experience designed just for you.</p>
    <p class="about__label">Target Market(s)</p>
    <p class="about__text">Our target market includes car owners of all price ranges, with a special focus on those who are passionate about their vehicles. We cater to clients who value excellent service and results, and seek to maintain their cars in pristine condition.</p>
  </article>

  <article class="panel contact">
    <div class="contact__grid">
      <span class="photo photo--dark" role="img" aria-label="Detailing product on orange microfibre cloth"></span>
      <span class="photo photo--grey" role="img" aria-label="Foam hand wash of a wheel"></span>
      <span class="photo photo--grey" role="img" aria-label="Foam-covered bonnet being washed"></span>
      <span class="photo photo--grey" role="img" aria-label="Hand cleaning an alloy wheel"></span>
    </div>
    <div class="contact__body">
      <div class="brandmark"><span class="brandmark__dot"></span><span class="brandmark__name">VELVET CREST</span></div>
      <p class="contact__line"><span class="contact__key">Address :</span> Rue des Saules 12, 1205 Geneva</p>
      <p class="contact__line"><span class="contact__key">Call :</span> +41 22 555 01 48</p>
      <p class="contact__line"><span class="contact__key">Opening hours :</span> Mon–Sat 8:00–18:30</p>
      <p class="contact__line"><span class="contact__key">E mail :</span> hello@velvetcrest.ch</p>
      <p class="contact__line"><span class="contact__key">Website :</span> www.velvetcrest.ch</p>
      <p class="contact__line"><span class="contact__key">Instagram :</span> @velvetcrest.geneva</p>
    </div>
  </article>

  <article class="panel cover">
    <svg class="cover__top" viewBox="0 0 380 70" aria-hidden="true">
      <defs><linearGradient id="coverWave" x1="0" y1="0" x2="1" y2="0"><stop offset="0" stop-color="#4f7fd3"/><stop offset=".5" stop-color="#8a55bf"/><stop offset="1" stop-color="#d43fa6"/></linearGradient></defs>
      <path d="M0 0H380V10C330 60 250 40 190 60 120 80 60 40 0 70Z" fill="url(#coverWave)" opacity=".85"/>
    </svg>
    <div class="cover__brand">
      <span class="cover__ring"></span>
      <p class="cover__name">VELVET<br>CREST</p>
    </div>
    <span class="cover__photo" role="img" aria-label="Red car driving through a water splash"></span>
    <ul class="cover__services">
      <li>DETAILING &amp; HAND WASH</li>
      <li>POLISHING</li>
      <li>CERAMIC TREATMENT</li>
      <li>PROTECTION FILM</li>
      <li>DETAILING BOUTIQUE</li>
    </ul>
    <svg class="cover__bottom" viewBox="0 0 380 40" aria-hidden="true">
      <defs><linearGradient id="coverBase" x1="0" y1="0" x2="1" y2="0"><stop offset="0" stop-color="#d43fa6"/><stop offset="1" stop-color="#4f7fd3"/></linearGradient></defs>
      <path d="M0 40V30C120 0 260 0 380 20V40Z" fill="#e873c2"/>
      <path d="M0 40V34C120 10 260 10 380 28V40Z" fill="url(#coverBase)"/>
    </svg>
  </article>
</section>

<!-- INSIDE -->
<section class="spread spread--inside">
  <article class="panel inside">
    <h2 class="services__title">SERVICES:</h2>
    <h3 class="service__title service__title--center">DETAILING &amp; HAND WASH</h3>
    <div class="pair">
      <span class="photo photo--grey" role="img" aria-label="Machine polisher working on car seat"></span>
      <span class="photo photo--dark" role="img" aria-label="Wash mitt cleaning a wheel"></span>
    </div>
    <ul class="bullets">
      <li>Comprehensive exterior &amp; interior care</li>
      <li>Personalisation and tailored cleaning packages</li>
      <li>Decontamination</li>
      <li>Premium products</li>
      <li>Attention to detail for a perfect finish</li>
    </ul>
    <h3 class="service__title" style="margin-top:10px">POLISHING</h3>
    <div class="row">
      <span class="photo photo--dark" style="width:118px;height:112px;flex:none" role="img" aria-label="Rotary polisher on car paint"></span>
      <ul class="bullets">
        <li>Eliminates scratches, holograms</li>
        <li>Revives and protects paint</li>
        <li>Ensures lasting gloss</li>
        <li>Enhances paint life</li>
        <li>Preserves car’s value and beauty</li>
      </ul>
    </div>
  </article>

  <article class="panel inside inside--mid">
    <span class="photo photo--dark ceramic__photo" role="img" aria-label="Dark car bonnet half treated with ceramic coating"></span>
    <div class="mid__body">
      <h3 class="service__title">CERAMIC TREATMENT</h3>
      <ul class="bullets">
        <li>Durable paint protection</li>
        <li>Water-repellent (hydrophobic) effect</li>
        <li>Easier cleaning, enhanced shine</li>
        <li>Long-term surface safeguarding</li>
        <li>Shields against environmental impacts</li>
      </ul>
      <div class="dryice">
        <span class="photo photo--grey dryice__photo" role="img" aria-label="Dry ice blasting machine"></span>
        <h3 class="dryice__title">DRY<br>ICE<br>WASH</h3>
      </div>
      <ul class="bullets">
        <li>Innovative, waterless method</li>
        <li>Safe for all car parts</li>
        <li>Deep cleans, removes odors</li>
        <li>Allergen-free, antibacterial</li>
        <li>Gentle, effective</li>
        <li>Advanced cleaning technology</li>
      </ul>
    </div>
  </article>

  <article class="panel inside inside--right">
    <h3 class="service__title">COVERING</h3>
    <ul class="bullets">
      <li>Personalized vehicle styling</li>
      <li>More than 150 colours available</li>
      <li>Clean cut without using a cutter</li>
      <li>High-quality, durable materials</li>
      <li>Custom designs available</li>
    </ul>
    <div class="pair" style="margin-top:6px">
      <span class="photo photo--blue" style="height:56px" role="img" aria-label="Car being wrapped in blue film"></span>
      <span class="photo photo--colour" style="height:56px" role="img" aria-label="Car with colourful custom wrap"></span>
    </div>
    <h3 class="service__title">DETAILING BOUTIQUE</h3>
    <ul class="bullets">
      <li>Premium brands available</li>
      <li>Buy on site during your visit</li>
      <li>Marble Harbour, Zeb Autos, DRUP Polaro</li>
    </ul>
    <div class="brands">
      <span class="brands__badge"></span>
      <span class="brands__badge"></span>
      <span class="brands__badge brands__badge--dark"></span>
    </div>
    <ul class="bullets">
      <li>Essential for at-home car care</li>
      <li>Perfect for quick touch-ups</li>
    </ul>
    <div class="row" style="margin-top:4px">
      <div style="flex:1">
        <h3 class="service__title">PROTECTION FILM</h3>
        <ul class="bullets">
          <li>Invisible, durable shield</li>
          <li>Self-healing technology</li>
          <li>10-year warranty by QR VONT</li>
        </ul>
      </div>
      <span class="photo photo--grey" style="width:110px;height:92px;flex:none" role="img" aria-label="Hands applying clear protection film"></span>
    </div>
  </article>
</section>

</body>
</html>
```